After tattoo calming solution

The label has to be modern, along the same lines as skin care brand “Plain Form.” It has to reflect the solutions natural effectiveness and simplicity. The label cannot be over fussy, and must be a little bit clinical, as it really does work. The colours should reflect that the solution calms the skin.

We use a 100ml spray bottle.

Target Market(s)

Anyone with a new tattoo or piercing

Industry/Entity Type

Skincare

Requirements
Must have
• Must reflect its natural calming but still remain a little clinical
Should not have
• It must not look like other flowery tattoo cream solutions.

```html
<!DOCTYPE html>
<html lang="en">
<head>
<meta charset="utf-8">
<title>After Tattoo &amp; Piercings — Box Front Label</title>
<link href="https://fonts.googleapis.com/css2?family=Montserrat:wght@500;700&display=swap" rel="stylesheet">
<style>
  :root {
    --backdrop: #cfcfcf;
    --label-white: #e3e3e3;
    --calm-teal: #4b9fa1;
    --ink: #111111;
  }
  html, body {
    margin: 0;
    padding: 0;
    width: 1200px;
    height: 1200px;
    overflow: hidden;
    background: var(--backdrop);
    font-family: "Montserrat", Arial, sans-serif;
    color: var(--ink);
  }
  .box-front {
    position: absolute;
    left: 450px;
    top: 60px;
    width: 301px;
    height: 1080px;
    background: var(--label-white);
  }
  .side-stripe {
    position: absolute;
    left: 245px;
    top: 0;
    width: 32px;
    height: 100%;
    background: var(--calm-teal);
  }
  .tagline {
    position: absolute;
    left: 26px;
    top: 109px;
    margin: 0;
    font-weight: 700;
    font-size: 15.5px;
    line-height: 14.2px;
    letter-spacing: -0.1px;
  }
  .tagline-rule {
    position: absolute;
    left: 26px;
    top: 162px;
    width: 124px;
    height: 9px;
    background: var(--calm-teal);
  }
  .benefits {
    position: absolute;
    left: 26px;
    top: 184px;
    margin: 0;
    font-weight: 500;
    font-size: 10px;
    line-height: 10.6px;
  }
  .product-name {
    position: absolute;
    left: 26px;
    top: 515px;
    margin: 0;
    font-weight: 700;
    font-size: 23.5px;
    line-height: 20px;
    letter-spacing: -0.2px;
  }
  .product-rule {
    position: absolute;
    left: 26px;
    top: 565px;
    width: 147px;
    height: 4px;
    background: var(--calm-teal);
  }
  .volume {
    position: absolute;
    left: 26px;
    top: 964px;
    margin: 0;
    font-weight: 500;
    font-size: 9.5px;
  }
</style>
</head>
<body>
  <main class="box-front">
    <div class="side-stripe"></div>
    <h2 class="tagline">Expert Skin<br>For New Tattoos<br>&amp; Piercings</h2>
    <div class="tagline-rule"></div>
    <p class="benefits">Reduces Inflammation<br>Irritation and Encourages<br>Natural Skin Healing</p>
    <h1 class="product-name">AFTER TATTOO<br>&amp; PIERCINGS</h1>
    <div class="product-rule"></div>
    <p class="volume">100ML</p>
  </main>
</body>
</html>
```